Bluestone Advisory & Mgmt - Professional Business Cards

Hi!

I am a Real Estate Developer and Construction Consultant.

I have a lot of inspiration from previous designs and would be open to using the attached Designs as a starting point. I would like to see these styles incorporated into your designs.

I really need professional business card to go with it that includes my important info.

Look forward to seeing your designs!.

Target Market(s)

My Target market are building owners, lawyers, consultants.

Industry/Entity Type

Real Estate Development

Contact Information for Business Card

My Name: Dorian Pelkey
My Title: Principle
Company Name: Bluestone Advisory & Mgmt, LLC
Address: 348 West 71st Street, 9th FL New York, NY 10010
Mobile: 917.806.3971
Website: bam-hvx.example

Font styles to use
Serif
Sans Serif

Colors

Designer to choose colors to be used in the design.

Requirements
Must have
• Must incorporate the logo attached or have new that looks similar.
• Must use professional font that will be seen and judged by wealthy land owners and developers.
• Must incorporate some of the color green.
Should not have
• Photo's or pictures of people or buildings of any kind.

```html
<!DOCTYPE html>
<html lang="en">
<head>
<meta charset="utf-8">
<title>Bluestone Advisory &amp; Mgmt - Business Cards</title>
<link rel="stylesheet" href="https://fonts.googleapis.com/css2?family=Arimo:wght@400;700&display=swap">
<style>
  :root {
    --backdrop: #a9aeaf;
    --paper: #f1f1ee;
    --brand-green: #3fb36f;
    --edge-green: #1f7a45;
    --ink: #2b2b2b;
    --warm-grey: #9c9593;
  }
  * { box-sizing: border-box; margin: 0; padding: 0; }
  html, body {
    width: 1200px;
    height: 824px;
    overflow: hidden;
    background: var(--backdrop);
    font-family: "Arimo", Arial, sans-serif;
  }
  .sheet {
    position: relative;
    width: 1200px;
    height: 824px;
    display: flex;
    align-items: center;
    justify-content: center;
    gap: 60px;
  }
  .card {
    width: 500px;
    height: 286px;
    background: var(--paper);
    border-bottom: 6px solid var(--edge-green);
    box-shadow: 0 10px 24px rgba(0,0,0,0.18);
    display: flex;
    flex-direction: column;
    align-items: center;
    justify-content: center;
    text-align: center;
  }
  .card-front { padding-top: 10px; }
  .holder-name {
    color: var(--brand-green);
    font-weight: 700;
    font-size: 22px;
    letter-spacing: 0.2px;
  }
  .title-row {
    display: flex;
    align-items: center;
    gap: 12px;
    margin-top: 2px;
  }
  .title-rule {
    width: 70px;
    height: 1px;
    background: var(--brand-green);
  }
  .holder-title {
    color: var(--warm-grey);
    font-weight: 700;
    font-size: 15px;
  }
  .contact {
    margin-top: 14px;
    color: var(--ink);
    font-size: 15px;
    line-height: 1.45;
  }
  .card-back { gap: 14px; }
  .brand {
    display: flex;
    align-items: center;
    gap: 14px;
  }
  .brand-mark {
    width: 30px;
    height: 30px;
    background: var(--brand-green);
  }
  .brand-name {
    color: var(--brand-green);
    font-weight: 400;
    font-size: 28px;
    letter-spacing: 0.5px;
  }
</style>
</head>
<body>
  <main class="sheet">
    <section class="card card-front">
      <h1 class="holder-name">Dorian Pelkey</h1>
      <div class="title-row">
        <span class="title-rule"></span>
        <span class="holder-title">Principle</span>
        <span class="title-rule"></span>
      </div>
      <p class="contact">
        Bluestone Advisory &amp; Mgmt, LLC<br>
        348 West 71st Street, 9th FL, New York, NY 10010<br>
        P. 917.806.3971 W.bam-hvx.example
      </p>
    </section>
    <section class="card card-back">
      <div class="brand">
        <span class="brand-mark"></span>
        <span class="brand-name">Bluestone Advisory Management</span>
      </div>
    </section>
  </main>
</body>
</html>
```